Winterization checkup email mail out

I have a handyman business and I want to design an email that will be sent out every month to our clients, so we will need a start design and are doing a home winterization package for residential clients, we are going to sell our "winterization package consultation" for $1 we will assess the clients house for what needs to be done every year for prevention, I want to have a cartoon "ish" look to it and round circles "buttons" with the sign for plumbing, electrical, freezing, cold and etc and a slogan for the campaign. I will be uploading our company logo and name.
Updates

I also uploaded pictures of our van and there is also a list of what are we looking to get it done in the "estimate", we would like to incorporate our van pictures in the design as well. Here is a description of the items we are going to be selling and that need to be incorporated into the design: Winterization checkup Is your house prepped for winter? Get started with a winterization checkup before the cold hits. What we look for: Window exterior sealing Drafts coming in from power outlets, electrical, gas and water lines Identify energy-inefficient red flags such as in-window air conditioning units left Gutter: check condition, and/or for caps or gutter protection Chimney, make sure is clean and shut is closed. Chimney and cap Vent cover condition, and attachment to chimney or vent pipes. Plumbing shut off valves Loose siding, flashing, and trim Recommendations for preventive measures, where applicable: Offer suggestions to homeowner about different new products that can help their house be more energy efficient and sealed for winter as of: Spray insulation, that can be applied to the walls to prevent cold climate. (example of ) Recommend preventive measures such as roof cables to prevent snow build up of ice dams. Inspect and reinforce railings (Deck, exterior stairs) AVOID: Expensive plumbing repairs from frozen pipes High energy bills from not properly sealed insulated doors and windows Hazards from dangerous falling gutter ice dams

Industry/Entity Type

Handyman

Font styles to use
Serif

Requirements
Must have
• I am picturing a cartoon "ish" house in the back with most common winter in USA problems in the east coast, frozen pipes, ventilation and so on, here are some samples of the checklist:
• Winterization checkup
• Is your house prepped for winter? Get started with a winterization checkup before the cold hits.
• AVOID:
• Expensive plumbing repairs from frozen pipes
• High energy bills from not properly sealed insulated doors and windows
• Hazards from dangerous falling gutter ice dams
• What we look for:
• Window exterior sealing
• Drafts coming in from power outlets, electrical, gas and water lines
• Identify energy-inefficient red flags such as in-window air conditioning units left
• Gutter: check condition, and/or for caps or gutter protection
• Chimney, make sure is clean and shut is closed.
• Chimney and cap
• Vent cover condition, and attachment to chimney or vent pipes.
• Plumbing shut off valves
• Loose siding, flashing, and trim
• Recommendations for preventive measures, where applicable:
• Offer suggestions to homeowner about different new products that can help their house be more energy efficient and sealed for winter as of:
• Spray insulation, that can be applied to the walls to prevent cold climate. (example of )
• Recommend preventive measures such as roof cables to prevent snow build up of ice dams.
• Inspect and reinforce railings (Deck, exterior stairs)
Nice to have
• Smart use of the company logo and colors, since this is going to be a montly email, I would like to have aspects that can be easily edited so we can re use the same email to highlithg other material as well within the same Fall, winter Theme

```html
<!DOCTYPE html>
<html lang="en">
<head>
<meta charset="utf-8">
<title>Hearthwise – Winterization Checkup</title>
<link href="https://fonts.googleapis.com/css2?family=Montserrat:wght@400;500;600;700;800&display=swap" rel="stylesheet">
<style>
  :root{
    --red:#dc343c;
    --red-deep:#d22f37;
    --bar-1:#d45a6b;
    --bar-2:#d64a56;
    --bar-3:#dc3540;
    --stone:#abaaa2;
    --paper:#f1f1f1;
    --white:#ffffff;
    --ink:#151515;
    --bar-text:#f6dcdf;
  }
  *{box-sizing:border-box;margin:0;padding:0}
  html,body{width:1200px;height:2439px;overflow:hidden;background:var(--white)}
  body{font-family:"Montserrat",Arial,sans-serif;color:var(--ink);position:relative}

  .masthead{position:absolute;left:0;top:0;width:1200px;height:177px;background:var(--white);text-align:center}
  .brand{position:absolute;left:0;right:0;top:38px;display:flex;justify-content:center;align-items:center;gap:12px}
  .brand-dot{width:34px;height:34px;border-radius:50%;background:var(--red)}
  .brand-name{font-weight:800;font-size:40px;color:var(--ink);letter-spacing:-0.5px}
  .tagline{position:absolute;left:0;right:0;top:103px;font-size:28px;font-weight:500;color:var(--ink)}

  .service-strip{position:absolute;left:0;top:177px;width:1200px;height:106px;background:var(--red)}
  .service-strip svg{position:absolute;top:14px}

  .hero{position:absolute;left:0;top:283px;width:1200px;height:553px;background:var(--stone)}
  .hero-art{position:absolute;left:0;top:0;width:725px;height:553px;
    background:radial-gradient(ellipse at 52% 55%,#d23a3c 0%,#c94448 28%,#b7a9a4 55%,var(--stone) 75%)}
  .hero-title{position:absolute;left:729px;top:155px;font-size:52px;font-weight:700;line-height:1.13;color:var(--red);text-transform:uppercase}
  .hero-offer{position:absolute;left:729px;top:320px;font-size:35px;font-weight:700;line-height:1.25;color:var(--ink)}

  .cta-band{position:absolute;left:0;top:836px;width:1200px;height:81px;background:var(--red)}
  .btn{position:absolute;display:flex;align-items:center;justify-content:center;font-weight:500;letter-spacing:1.5px;text-transform:uppercase;border-radius:6px}
  .btn-light{left:427px;top:12px;width:309px;height:56px;border:2px solid #f3b5b9;color:var(--white);font-size:22px}
  .btn-outline{border:2px solid #e58a90;color:var(--red);font-size:21px;height:42px;width:244px}

  .feature{position:absolute;left:0;width:1200px;height:543px}
  .feature-plumbing{top:917px}
  .feature-electric{top:1460px}
  .feature-icon{position:absolute;top:0;width:591px;height:543px;background:var(--red)}
  .feature-copy{position:absolute;top:0;width:609px;height:543px;background:var(--paper)}
  .feature-plumbing .feature-icon{left:0}
  .feature-plumbing .feature-copy{left:591px}
  .feature-electric .feature-copy{left:0;width:591px}
  .feature-electric .feature-icon{left:591px;width:609px}
  .feature-icon svg{position:absolute}

  .feature-title{position:absolute;font-weight:700;color:var(--red);line-height:1.15}
  .feature-text{position:absolute;font-size:31px;font-weight:400;color:var(--ink);line-height:1.15}
  .feature-price{position:absolute;font-size:51px;font-weight:700;color:var(--red)}

  .feature-plumbing .feature-title{left:75px;top:68px;font-size:53px}
  .feature-plumbing .feature-title small{display:block;font-size:40px;margin-top:8px}
  .feature-plumbing .feature-text{left:75px;top:266px}
  .feature-plumbing .feature-price{left:85px;top:360px}
  .feature-plumbing .btn{left:83px;top:457px}

  .feature-electric .feature-title{left:46px;top:65px;font-size:56px;width:520px}
  .feature-electric .feature-text{left:57px;top:200px;width:480px}
  .feature-electric .feature-price{left:55px;top:350px}
  .feature-electric .btn{left:57px;top:446px}

  .service-list{position:absolute;left:0;top:2003px;width:1200px;height:436px}
  .service-bar{height:145.4px;display:flex;align-items:center;justify-content:center;font-size:46px;font-weight:500;letter-spacing:4px;color:var(--bar-text);text-transform:uppercase}
  .service-bar:nth-child(1){background:var(--bar-1)}
  .service-bar:nth-child(2){background:var(--bar-2)}
  .service-bar:nth-child(3){background:var(--bar-3)}
</style>
</head>
<body>

<header class="masthead">
  <div class="brand"><span class="brand-dot"></span><span class="brand-name">Hearthwise</span></div>
  <p class="tagline">Helping you looking after your home</p>
</header>

<nav class="service-strip" aria-label="Services">
  <svg style="left:314px" width="80" height="80" viewBox="0 0 80 80" aria-label="Appliances">
    <circle cx="40" cy="40" r="38" fill="none" stroke="#fff" stroke-width="2"/>
    <rect x="24" y="19" width="32" height="42" rx="3" fill="none" stroke="#fff" stroke-width="3"/>
    <line x1="24" y1="31" x2="56" y2="31" stroke="#fff" stroke-width="3"/>
    <circle cx="44" cy="46" r="8" fill="none" stroke="#fff" stroke-width="3"/>
  </svg>
  <svg style="left:491px" width="80" height="80" viewBox="0 0 80 80" aria-label="Electrical">
    <circle cx="40" cy="40" r="38" fill="none" stroke="#fff" stroke-width="2"/>
    <path d="M40 16c-11 0-19 8-19 18 0 13 19 30 19 30s19-17 19-30c0-10-8-18-19-18z" fill="#fff"/>
    <path d="M43 22l-10 16h7l-4 15 11-18h-7z" fill="var(--red)"/>
  </svg>
  <svg style="left:663px" width="80" height="80" viewBox="0 0 80 80" aria-label="Plumbing">
    <circle cx="40" cy="40" r="38" fill="none" stroke="#fff" stroke-width="2"/>
    <path d="M40 18L18 38h6v22h32V38h6z" fill="#fff"/>
    <path d="M40 36c-4 6-6 9-6 12a6 6 0 0012 0c0-3-2-6-6-12z" fill="var(--red)"/>
  </svg>
  <svg style="left:863px" width="80" height="80" viewBox="0 0 80 80" aria-label="Heating">
    <circle cx="40" cy="40" r="38" fill="none" stroke="#fff" stroke-width="2"/>
    <g fill="#fff"><rect x="22" y="20" width="5" height="36" rx="2"/><rect x="30" y="20" width="5" height="36" rx="2"/><rect x="38" y="20" width="5" height="36" rx="2"/><rect x="46" y="20" width="5" height="36" rx="2"/></g>
    <circle cx="52" cy="52" r="8" fill="var(--red)" stroke="#fff" stroke-width="3"/>
  </svg>
</nav>

<section class="hero">
  <div class="hero-art" role="img" aria-label="Cartoon red house wearing a knitted hat, earmuffs and scarf under snowy clouds"></div>
  <h1 class="hero-title">Is your home<br>winter ready?</h1>
  <p class="hero-offer">Get Your Winterization<br>package consultation<br>FOR JUST $1</p>
</section>

<div class="cta-band"><a class="btn btn-light">Get it now for $1</a></div>

<section class="feature feature-plumbing">
  <div class="feature-icon">
    <svg style="left:110px;top:60px" width="364" height="364" viewBox="0 0 364 364" aria-label="Plumbing">
      <circle cx="182" cy="182" r="181" fill="none" stroke="#f0a0a5" stroke-width="2"/>
      <path d="M182 72L58 182h26v110h196V182h26l-36-32V96h-26v32z" fill="#fff" stroke="#fff" stroke-width="10" stroke-linejoin="round"/>
      <path d="M182 160c-18 26-28 42-28 56a28 28 0 0056 0c0-14-10-30-28-56z" fill="var(--red)"/>
    </svg>
  </div>
  <div class="feature-copy">
    <h2 class="feature-title">Is your plumbing<small>up the the standards</small></h2>
    <p class="feature-text">You must be regulated by law</p>
    <p class="feature-price">$1 consultation</p>
    <a class="btn btn-outline">Get it now</a>
  </div>
</section>

<section class="feature feature-electric">
  <div class="feature-copy">
    <h2 class="feature-title">Winter is not the time for risks</h2>
    <p class="feature-text">Make sure your electrical fundations are in place</p>
    <p class="feature-price">$1 consultation</p>
    <a class="btn btn-outline">Get it now</a>
  </div>
  <div class="feature-icon">
    <svg style="left:96px;top:89px" width="364" height="364" viewBox="0 0 364 364" aria-label="Electrical">
      <circle cx="182" cy="182" r="181" fill="none" stroke="#f0a0a5" stroke-width="2"/>
      <path d="M180 62c-52 0-92 40-92 88 0 56 92 160 92 160 4 4 14 4 18-2 6-8 74-98 74-158 0-48-40-88-92-88z" fill="#fff"/>
      <path d="M200 86l-52 86h36l-22 94 66-112h-36z" fill="var(--red)"/>
    </svg>
  </div>
</section>

<section class="service-list" aria-label="Checks">
  <div class="service-bar">Plumbing</div>
  <div class="service-bar">Electrical check</div>
  <div class="service-bar">Pressure check</div>
</section>

</body>
</html>
```